Business card design needed

We are a boutique law firm within the Melbourne CBD.

You will need to upload our company logo which is to go on the left hand side of the business card - we then have a Legal Guild of Carrowmere logo to go perhaps on the bottom right hand side (color)

On the back we would like the website details

www.hartwellsolicitors.com.au - with a small logo
Updates

Thank you designers for all your great submissions.  Just going through the designs and we will choose one within the next couple of days.

Kind Regards
Hartwells Solicitors Pty Ltd

Industry/Entity Type

Boutique

Contact Information for Business Card

Dominic Hartwell
Principal
Level 6, 47 Penrose Street
Melbourne VIC Australia 3000
T+61 3 9555 0142 F+61 3 9555 0187
dominic@hartwellsolicitors.com.au
M 0491 570 156

```html
<!DOCTYPE html>
<html lang="en">
<head>
<meta charset="utf-8">
<title>Hartwells Solicitors – Business Card</title>
<link rel="stylesheet" href="https://fonts.googleapis.com/css2?family=Questrial&display=swap">
<style>
  :root {
    --canvas: #3b2f28;
    --card: #050505;
    --gold-dark: #6b5234;
    --gold-mid: #b8966a;
    --gold-light: #f0dcb8;
    --gold-text: #a98a5e;
    --white: #f2f2f2;
    --grey: #a7a7a7;
    --rule: #6b5a44;
    --badge: #e9e9e9;
    --gold-sheen: linear-gradient(100deg, var(--gold-dark) 0%, var(--gold-mid) 35%, var(--gold-light) 55%, var(--gold-mid) 75%, var(--gold-dark) 100%);
  }
  * { margin: 0; padding: 0; box-sizing: border-box; }
  html, body { width: 1200px; height: 900px; overflow: hidden; }
  body {
    background: var(--canvas);
    font-family: "Questrial", "Century Gothic", sans-serif;
    position: relative;
  }
  .card {
    position: absolute;
    width: 620px;
    height: 354px;
    background: var(--card);
    overflow: hidden;
    box-shadow: 0 12px 30px rgba(0,0,0,.45);
  }
  .card--back { left: 60px; top: 50px; }
  .card--front { left: 520px; top: 496px; }

  .gold-band { position: absolute; background: var(--gold-sheen); }
  .card--back .gold-band--top { left: 330px; top: 52px; width: 290px; height: 58px; }
  .card--back .gold-band--left { left: 0; top: 228px; width: 92px; height: 44px; }
  .card--front .gold-band--top { left: 330px; top: 40px; width: 290px; height: 58px; }
  .card--front .gold-band--left { left: 0; top: 142px; width: 92px; height: 46px; }

  .brand-name {
    position: absolute;
    font-size: 30px;
    letter-spacing: .5px;
    color: var(--gold-mid);
    display: flex;
    align-items: center;
    gap: 10px;
  }
  .brand-name .mark { width: 14px; height: 14px; background: var(--gold-mid); }
  .card--back .brand-name--main { left: 108px; top: 218px; }
  .card--front .brand-name--main { left: 108px; top: 140px; }

  .brand-name--small {
    left: 370px; top: 134px;
    font-size: 20px;
    color: var(--white);
  }
  .partner-badge {
    position: absolute;
    left: 500px; top: 122px;
    width: 56px; height: 56px;
    background: var(--badge);
  }
  .partner-badge::after {
    content: "";
    position: absolute;
    inset: 12px;
    border-radius: 50%;
    background: #3b6fa3;
  }
  .website {
    position: absolute;
    left: 100px; top: 296px;
    font-size: 17px;
    letter-spacing: 1px;
    color: var(--gold-text);
  }

  .contact-divider {
    position: absolute;
    left: 330px; top: 150px;
    width: 1px; height: 100px;
    background: var(--rule);
  }
  .contact-list {
    position: absolute;
    left: 346px; top: 150px;
    list-style: none;
    font-size: 14.5px;
    color: var(--white);
  }
  .contact-list li {
    display: flex; align-items: center; gap: 14px;
    height: 22px;
  }
  .contact-list svg { width: 12px; height: 12px; flex: none; }
  .contact-rule {
    position: absolute;
    left: 346px; top: 260px;
    width: 250px; height: 1px;
    background: var(--rule);
  }
  .person-name {
    position: absolute;
    left: 110px; top: 232px;
    font-size: 21px;
    color: var(--white);
  }
  .footer-rule {
    position: absolute;
    left: 24px; top: 316px;
    width: 572px; height: 1px;
    background: var(--rule);
  }
  .footer-line {
    position: absolute;
    left: 24px; top: 324px;
    font-size: 12.5px;
    color: var(--grey);
    white-space: nowrap;
  }
</style>
</head>
<body>

  <section class="card card--back" aria-label="Card back">
    <div class="gold-band gold-band--top"></div>
    <div class="gold-band gold-band--left"></div>
    <div class="brand-name brand-name--main"><span class="mark"></span>Hartwells</div>
    <div class="brand-name brand-name--small">Hartwells</div>
    <div class="partner-badge" role="img" aria-label="Legal Guild of Carrowmere accreditation badge"></div>
    <p class="website">www.hartwellsolicitors.com.au</p>
  </section>

  <section class="card card--front" aria-label="Card front">
    <div class="gold-band gold-band--top"></div>
    <div class="gold-band gold-band--left"></div>
    <div class="brand-name brand-name--main"><span class="mark"></span>Hartwells</div>

    <div class="contact-divider"></div>
    <ul class="contact-list">
      <li>
        <svg viewBox="0 0 12 12" aria-label="Mobile"><rect x="3" y="0.5" width="6" height="11" rx="1" fill="none" stroke="#f2f2f2"/><line x1="5" y1="9.5" x2="7" y2="9.5" stroke="#f2f2f2"/></svg>
        0491 570 156
      </li>
      <li>
        <svg viewBox="0 0 12 12" aria-label="Telephone"><path d="M2 1.5 L4.5 1.5 L5.5 4 L4 5 Q5 7.5 7 8 L8 6.5 L10.5 7.5 L10.5 10 Q5 11 2 6 Z" fill="none" stroke="#f2f2f2"/></svg>
        +61 3 9555 0142
      </li>
      <li>
        <svg viewBox="0 0 12 12" aria-label="Fax"><rect x="3" y="0.5" width="6" height="4" fill="none" stroke="#f2f2f2"/><rect x="0.5" y="4.5" width="11" height="5" fill="none" stroke="#f2f2f2"/><rect x="3" y="8" width="6" height="3.5" fill="#f2f2f2"/></svg>
        +61 3 9555 0187
      </li>
      <li>
        <svg viewBox="0 0 12 12" aria-label="Email"><text x="0" y="10.5" font-size="12" fill="#f2f2f2" font-family="sans-serif">@</text></svg>
        dominic@hartwellsolicitors.com.au
      </li>
    </ul>
    <div class="contact-rule"></div>

    <p class="person-name">Dominic Hartwell</p>

    <div class="footer-rule"></div>
    <p class="footer-line">Principal Hartwells Solicitors Pty Ltd Level 6, 47 Penrose Street Melbourne VIC Australia 3000</p>
  </section>

</body>
</html>
```